Hero Image for Homepage Header

I need an hero image (main image) for a new web site.
The site will be a sales consultancy/coaching business aimed at B2B software sales professionals and software/SaaS firms. The aim of the business is to help sales professionals and tech firms transform their sales performance and close more deals.

The two styles of hero images I like can be seen here:
- Plumvane.com
- Dottrick.com

You can come up with a concept that is like one of these.

Basically the image should show a familiar UI screen of a sales professional's CRM dashboard (see attachments).
In the animated gif (which I hate - it's poor quality) you can see how the data points all improve. This represents the sales 'transformation'.

I'd like you to re-create a UI screen from orbelwick.com (the attachments, Orbelwick1 and Orbelwick2 are taken from the Orbelwick CRM software. I want you to recreate them from scratch but in a more high-quality manner and come up with a hero image design concept that will show how poor results on screen can become better.
The attachment Orbelwick2 shows how the results from Orbelwick1 have been improved.

If you think an animated gif would be better, that's fine.

I'd like your design concept to include the following points (in freehand text style just like in the Plumvane.com image)

- 4x pipeline
- Higher conversions
- More deals CLOSED-WON

Come up with something stunning

```html
<!DOCTYPE html>
<html lang="en">
<head>
<meta charset="utf-8">
<title>Sales Coaching – Hero</title>
<link rel="stylesheet" href="https://fonts.googleapis.com/css2?family=Roboto+Condensed:wght@400;700&family=Jost:wght@400;500&family=Arimo:wght@400;700&display=swap">
<style>
  :root {
    --sky-light: #a9d3ee;
    --sky-mid: #3f8fcb;
    --deep-blue: #1559a0;
    --navy-text: #2a2163;
    --white: #ffffff;
    --button-blue: #0f4f98;
    --bullet-blue: #63b6e3;
    --panel-border: #e2e4e8;
    --ink: #2b2f36;
    --muted: #7a808a;
    --link: #1a8ac9;
    --gauge-red: #c62a2a;
    --gauge-orange: #f2a23a;
    --gauge-green: #17695a;
    --stage-1: #1ea0dc;
    --stage-2: #1b2a55;
    --stage-3: #80d2d0;
    --stage-4: #17a898;
    --stage-5: #e6cf7a;
    --stage-6: #f0a030;
  }
  * { box-sizing: border-box; margin: 0; padding: 0; }
  html, body { width: 1200px; height: 848px; overflow: hidden; }
  body { position: relative; font-family: "Jost", sans-serif; }

  .hero-backdrop {
    position: absolute; inset: 0;
    background:
      linear-gradient(160deg, rgba(255,255,255,0.25) 0%, rgba(255,255,255,0) 30%),
      linear-gradient(200deg, rgba(14,70,140,0) 55%, rgba(30,80,140,0.35) 100%),
      linear-gradient(180deg, var(--sky-light) 0%, var(--sky-mid) 30%, var(--deep-blue) 55%, #3a79b4 80%, #7ea9cf 100%);
  }

  .brand {
    position: absolute; left: 27px; top: 36px;
    font-family: "Roboto Condensed", sans-serif; font-weight: 400;
    font-size: 56px; color: var(--white); letter-spacing: 1px;
  }
  .main-nav {
    position: absolute; top: 46px; left: 0; width: 1200px; height: 40px;
    font-family: "Roboto Condensed", sans-serif; font-size: 37px; color: #111;
  }
  .main-nav a { position: absolute; color: inherit; text-decoration: none; }

  .headline {
    position: absolute; left: 0; top: 196px; width: 1200px; height: 160px;
    font-family: "Roboto Condensed", sans-serif; color: var(--navy-text);
    font-size: 80px; line-height: 76px; font-weight: 400;
  }
  .headline .line {
    position: absolute; left: 0; width: 1200px; text-align: center; white-space: nowrap;
    transform-origin: 50% 50%;
  }
  .headline .line-one { top: 6px; left: -10px; transform: scaleX(0.93); letter-spacing: -0.5px; }
  .headline .line-two { top: 82px; transform: scaleX(0.95); }
  .headline strong { color: var(--white); font-weight: 700; }

  .mission {
    position: absolute; left: 38px; top: 400px; width: 400px;
    color: var(--white); font-size: 37px; line-height: 40.5px; font-weight: 400;
    letter-spacing: 0.4px;
  }
  .cta {
    position: absolute; left: 31px; top: 682px; width: 170px; height: 42px;
    border-radius: 21px; background: var(--button-blue); color: var(--white);
    font-size: 27px; line-height: 42px; text-align: center; letter-spacing: 1px;
  }
  .outcomes { position: absolute; top: 764px; left: 0; height: 34px; width: 1200px; color: #0d0d0d; font-size: 28px; letter-spacing: 0; }
  .outcomes span { position: absolute; top: 0; white-space: nowrap; }
  .outcomes i { position: absolute; top: 9px; width: 21px; height: 21px; background: var(--bullet-blue); }

  .crm-dashboard {
    position: absolute; left: 440px; top: 388px; width: 740px; height: 301px;
    background: var(--white); font-family: "Arimo", sans-serif; color: var(--ink);
  }
  .dash-header {
    position: absolute; left: 8px; top: 7px; width: 725px; height: 25px;
    border: 1px solid var(--panel-border); background: #f7f8fa;
  }
  .dash-header .badge { position: absolute; left: 4px; top: 3px; width: 10px; height: 10px; background: #e0463a; border-radius: 2px; }
  .dash-header .crumb { position: absolute; left: 18px; top: 2px; font-size: 4.5px; color: var(--muted); }
  .dash-header .title { position: absolute; left: 18px; top: 7px; font-size: 6px; font-weight: 700; }
  .dash-header .meta { position: absolute; left: 4px; top: 16px; font-size: 4.5px; color: var(--muted); }
  .dash-header .meta b { color: var(--link); font-weight: 400; }
  .dash-header .btns { position: absolute; right: 10px; top: 4px; display: flex; }
  .dash-header .btns span { border: 1px solid var(--panel-border); background: #fff; font-size: 5px; padding: 3px 6px; }

  .panel { position: absolute; border: 1px solid var(--panel-border); background: #fff; }
  .panel h3 { position: absolute; left: 5px; top: 5px; font-size: 6px; font-weight: 700; }
  .panel h4 { position: absolute; left: 5px; top: 13px; font-size: 4.5px; font-weight: 400; color: var(--muted); }
  .panel .drill { position: absolute; left: 5px; bottom: 12px; font-size: 4.5px; color: var(--muted); }
  .panel .report { position: absolute; left: 5px; bottom: 5px; font-size: 4.3px; color: var(--link); }
  .panel svg { position: absolute; left: 0; top: 0; }

  .big-figure { position: absolute; left: 0; width: 100%; top: 42px; text-align: center; font-family: "Arimo", sans-serif; color: var(--gauge-green); font-size: 38px; }
  .big-figure small { font-size: 24px; }

  .top-deals { position: absolute; left: 10px; top: 26px; width: 165px; border-collapse: collapse; font-size: 4.2px; }
  .top-deals th { background: #f1f2f4; text-align: left; font-weight: 400; color: var(--muted); padding: 2px 3px; }
  .top-deals td { color: var(--stage-4); padding: 0.5px 3px; border-bottom: 1px solid #eef0f2; }
  .top-deals td.num { color: var(--ink); text-align: right; }
</style>
</head>
<body>
  <div class="hero-backdrop" role="img" aria-label="Blue low-poly faceted background, light at top fading to deep blue"></div>

  <div class="brand">LOGO</div>
  <nav class="main-nav">
    <a style="left:579px">Product</a>
    <a style="left:761px">Learn</a>
    <a style="left:917px">Pricing</a>
    <a style="left:1088px">Login</a>
  </nav>

  <h1 class="headline">
    <span class="line line-one">B2b Software Sales Professionals</span>
    <span class="line line-two">and <strong>Software/Saas Firms</strong></span>
  </h1>

  <p class="mission">The aim of the business is to help sales professionals and tech firms transform their sales performance and close more deals.</p>

  <div class="cta">Know More</div>

  <div class="outcomes">
    <i style="left:51px"></i><span style="left:86px">4x pipeline</span>
    <i style="left:239px"></i><span style="left:277px">Higher conversions</span>
    <i style="left:519px"></i><span style="left:559px">More deals CLOSED-WON</span>
  </div>

  <section class="crm-dashboard">
    <header class="dash-header">
      <span class="badge"></span>
      <span class="crumb">Dashboard</span>
      <span class="title">Sales Rep Dashboard</span>
      <span class="meta">As of 23 August, 14:34 - Dana Hollis - <b>Change</b></span>
      <div class="btns"><span>Refresh</span><span>Edit</span><span>▾</span></div>
    </header>

    <div class="panel" style="left:7px;top:37px;width:214px;height:128px">
      <h3>MTD Total MRR</h3><h4>MTD Closed Won Opportunities</h4>
      <svg width="214" height="128" viewBox="0 0 214 128">
        <path d="M51 103 A58 58 0 0 1 73.7 40.5" fill="none" stroke="var(--gauge-red)" stroke-width="7"/>
        <path d="M73.7 40.5 A58 58 0 0 1 136 37.8" fill="none" stroke="var(--gauge-orange)" stroke-width="7"/>
        <path d="M136 37.8 A58 58 0 0 1 163 103" fill="none" stroke="var(--gauge-green)" stroke-width="7"/>
        <g font-size="3.5" fill="#b0b4ba" font-family="Arimo, sans-serif">
          <text x="60" y="98">$0</text><text x="58" y="82">$10K</text><text x="64" y="64">$30K</text>
          <text x="86" y="46">$50K</text><text x="120" y="46">$90K</text><text x="145" y="64">$110K</text><text x="148" y="90">$130K</text>
        </g>
        <polygon points="64.5,73.4 106,92 108,84" fill="var(--stage-2)"/>
        <text x="107" y="116" font-size="6" text-anchor="middle" fill="var(--gauge-green)" font-family="Arimo, sans-serif">$ 21K (16%)</text>
      </svg>
      <p class="drill">Drill into report to see details</p>
      <p class="report">View Report (SR: Closed Won Opportunities MRR)</p>
    </div>

    <div class="panel" style="left:224px;top:37px;width:320px;height:128px">
      <h3>MTD Your Pipeline Opportunities</h3><h4>MTD Your Pipeline Opportunities</h4>
      <svg width="320" height="128" viewBox="0 0 320 128" font-family="Arimo, sans-serif">
        <text x="159" y="24" font-size="4.5" text-anchor="middle" fill="#555">Sum of Amount</text>
        <polygon points="129,28 189,28 186,41 132,41" fill="var(--stage-1)"/>
        <polygon points="132,41 186,41 183,54 135,54" fill="var(--stage-2)"/>
        <polygon points="135,54 183,54 181,67 137,67" fill="var(--stage-3)"/>
        <polygon points="137,67 181,67 180,80 138,80" fill="var(--stage-4)"/>
        <polygon points="138,80 180,80 179,93 139,93" fill="var(--stage-5)"/>
        <polygon points="139,93 179,93 178,106 140,106" fill="var(--stage-6)"/>
        <g font-size="6" fill="#fff" text-anchor="middle">
          <text x="159" y="37">$ 7K</text><text x="159" y="50">$ 11K</text><text x="159" y="63">$ 9K</text>
          <text x="159" y="76">$ 29K</text><text x="159" y="89">$ 21K</text><text x="159" y="102">$ 9K</text>
        </g>
        <text x="304" y="24" font-size="5.5" text-anchor="end" fill="#333">Stage</text>
        <g font-size="4.5" fill="#444" text-anchor="end">
          <text x="300" y="34">Initial Contact</text><text x="300" y="44">Discovery Call</text><text x="300" y="53">Demo Delivered</text>
          <text x="300" y="62">Technical Validation</text><text x="300" y="71">Proposal</text><text x="300" y="81">Negotiation</text>
        </g>
        <rect x="304" y="30" width="5" height="5" fill="var(--stage-1)"/><rect x="304" y="40" width="5" height="5" fill="var(--stage-2)"/>
        <rect x="304" y="49" width="5" height="5" fill="var(--stage-3)"/><rect x="304" y="58" width="5" height="5" fill="var(--stage-4)"/>
        <rect x="304" y="67" width="5" height="5" fill="var(--stage-5)"/><rect x="304" y="77" width="5" height="5" fill="var(--stage-6)"/>
      </svg>
      <p class="drill">Drill into report to see details</p>
      <p class="report">View Report (SR: Your Pipeline Opportunities MTD)</p>
    </div>

    <div class="panel" style="left:547px;top:37px;width:186px;height:128px">
      <h3>FYTD Total ACV</h3><h4>FYTD Closed Won Opportunities</h4>
      <div class="big-figure">$1.1 <small>M</small></div>
      <p class="drill">Drill into report to see details</p>
      <p class="report">View Report (SR: Closed Won Opportunities ACV)</p>
    </div>

    <div class="panel" style="left:7px;top:168px;width:214px;height:128px">
      <h3>FYTD Total ARR</h3><h4>FYTD Closed Won Opportunities</h4>
      <svg width="214" height="128" viewBox="0 0 214 128">
        <path d="M51 103 A58 58 0 0 1 73.7 40.5" fill="none" stroke="var(--gauge-red)" stroke-width="7"/>
        <path d="M73.7 40.5 A58 58 0 0 1 136 37.8" fill="none" stroke="var(--gauge-orange)" stroke-width="7"/>
        <path d="M136 37.8 A58 58 0 0 1 163 103" fill="none" stroke="var(--gauge-green)" stroke-width="7"/>
        <g font-size="3.5" fill="#b0b4ba" font-family="Arimo, sans-serif">
          <text x="60" y="98">$0</text><text x="58" y="82">$100K</text><text x="64" y="64">$200K</text>
          <text x="86" y="46">$600K</text><text x="120" y="46">$1M</text><text x="145" y="64">$1.3M</text><text x="148" y="90">$1.5M</text>
        </g>
        <polygon points="102.3,43.2 103,92 111,92" fill="var(--stage-2)"/>
        <text x="107" y="116" font-size="6" text-anchor="middle" fill="var(--gauge-green)" font-family="Arimo, sans-serif">$ 726K (47%)</text>
      </svg>
      <p class="drill">Drill into report to see details</p>
      <p class="report">View Report (SR: Closed Won Opportunities ARR)</p>
    </div>

    <div class="panel" style="left:224px;top:168px;width:320px;height:128px">
      <h3>FYTD Your Pipeline Opportunities</h3><h4>FYTD Your Pipeline Opportunities</h4>
      <svg width="320" height="128" viewBox="0 0 320 128" font-family="Arimo, sans-serif">
        <text x="159" y="24" font-size="4.5" text-anchor="middle" fill="#555">Sum of Amount</text>
        <polygon points="129,28 189,28 186,41 132,41" fill="var(--stage-1)"/>
        <polygon points="132,41 186,41 183,54 135,54" fill="var(--stage-2)"/>
        <polygon points="135,54 183,54 181,67 137,67" fill="var(--stage-3)"/>
        <polygon points="137,67 181,67 180,80 138,80" fill="var(--stage-4)"/>
        <polygon points="138,80 180,80 179,93 139,93" fill="var(--stage-5)"/>
        <polygon points="139,93 179,93 178,106 140,106" fill="var(--stage-6)"/>
        <g font-size="6" fill="#fff" text-anchor="middle">
          <text x="159" y="37">$ 109K</text><text x="159" y="50">$ 118K</text><text x="159" y="63">$ 228K</text>
          <text x="159" y="76">$ 255K</text><text x="159" y="89">$ 204K</text><text x="159" y="102">$ 88K</text>
        </g>
        <text x="304" y="24" font-size="5.5" text-anchor="end" fill="#333">Stage</text>
        <g font-size="4.5" fill="#444" text-anchor="end">
          <text x="300" y="34">Initial Contact</text><text x="300" y="44">Discovery Call</text><text x="300" y="53">Demo Delivered</text>
          <text x="300" y="62">Technical Validation</text><text x="300" y="71">Proposal</text><text x="300" y="81">Negotiation</text>
        </g>
        <rect x="304" y="30" width="5" height="5" fill="var(--stage-1)"/><rect x="304" y="40" width="5" height="5" fill="var(--stage-2)"/>
        <rect x="304" y="49" width="5" height="5" fill="var(--stage-3)"/><rect x="304" y="58" width="5" height="5" fill="var(--stage-4)"/>
        <rect x="304" y="67" width="5" height="5" fill="var(--stage-5)"/><rect x="304" y="77" width="5" height="5" fill="var(--stage-6)"/>
      </svg>
      <p class="drill">Drill into report to see details</p>
      <p class="report">View Report (SR: Your Pipeline Opportunities FYTD)</p>
    </div>

    <div class="panel" style="left:547px;top:168px;width:186px;height:128px">
      <h3>Your 10 Opportunities</h3><h4>FYTD Top 10 Opportunities</h4>
      <table class="top-deals">
        <tr><th>Opportunity Name ↑</th><th>MRR</th><th>ARR</th></tr>
        <tr><td>Ravlor</td><td class="num">69k</td><td class="num">828k</td></tr>
        <tr><td>Quintar</td><td class="num">53k</td><td class="num">636k</td></tr>
        <tr><td>Brevalle</td><td class="num">46k</td><td class="num">552k</td></tr>
        <tr><td>Zentrix</td><td class="num">38k</td><td class="num">456k</td></tr>
        <tr><td>Calder Bank</td><td class="num">33k</td><td class="num">396k</td></tr>
        <tr><td>Mireth</td><td class="num">28k</td><td class="num">336k</td></tr>
        <tr><td>Tolvan</td><td class="num">28k</td><td class="num">336k</td></tr>
        <tr><td>Harbor Crest Health</td><td class="num">23k</td><td class="num">276k</td></tr>
        <tr><td>Fennmark</td><td class="num">21k</td><td class="num">252k</td></tr>
        <tr><td>Lumacell</td><td class="num">19k</td><td class="num">228k</td></tr>
      </table>
      <p class="drill">Drill into report to see details</p>
      <p class="report">View Report (SR: Your Top 10 Opportunities)</p>
    </div>
  </section>
</body>
</html>
```